Vehicle Wrap

Looking for a new design to our electrical vans. Partial wrap , sides and back - no front. Logo , Services offered , KRB & LMQ # , phone number and website. Needs to Use Pelvora logo as well.

```html
<!DOCTYPE html>
<html lang="en">
<head>
<meta charset="utf-8">
<title>Harbour Electric – Van Wrap Sides</title>
<link href="https://fonts.googleapis.com/css2?family=Montserrat:wght@600;700;800&display=swap" rel="stylesheet">
<style>
  :root{
    --ink:#231f1c;
    --ink-deep:#1a1714;
    --gold:#c9a227;
    --white:#ffffff;
    --trim:#2b2b2d;
    --tyre:#1c1c1e;
    --hub:#c9ccd0;
    --glass:#3a4148;
    --page:#eeeeec;
  }
  html,body{margin:0;padding:0;width:1187px;height:1200px;overflow:hidden;background:var(--page);}
  .wrap-sheet{width:1187px;height:1200px;display:flex;flex-direction:column;}
  .van-side{display:block;width:1187px;height:600px;}
  .txt{font-family:"Montserrat",sans-serif;}
  .tagline{fill:var(--gold);font-weight:700;font-size:26px;}
  .service-band-text{fill:var(--ink);font-weight:700;font-size:15px;}
  .web{fill:var(--gold);font-weight:600;font-size:15px;}
  .phone{fill:var(--gold);font-weight:700;font-size:28px;}
  .licence{fill:var(--gold);font-weight:700;font-size:12px;}
  .brand-name{fill:var(--gold);font-weight:800;font-size:44px;}
  .brand-sub{fill:var(--gold);font-weight:800;font-size:30px;letter-spacing:6px;}
  .partner-name{fill:var(--ink);font-weight:800;font-size:14px;}
  .partner-sub{fill:var(--ink);font-weight:700;font-size:7px;}
</style>
</head>
<body>
<main class="wrap-sheet">

  <!-- Passenger side (faces right) -->
  <svg class="van-side" viewBox="0 0 1187 600" xmlns="http://www.w3.org/2000/svg">
    <defs>
      <clipPath id="body-clip-a">
        <path d="M95,145 Q98,120 130,120 L905,120 Q960,124 990,200 L1035,330 Q1128,355 1140,400 L1146,470 Q1146,492 1120,492 L100,492 Q95,492 95,475 Z"/>
      </clipPath>
    </defs>
    <g class="van-body" clip-path="url(#body-clip-a)">
      <rect x="90" y="115" width="1060" height="385" fill="var(--white)"/>
      <polygon fill="var(--ink)" points="90,115 740,115 690,500 90,500"/>
      <polygon class="bolt" fill="var(--gold)" points="712,120 835,120 795,245 815,245 690,492 712,310 690,310"/>
      <rect x="90" y="440" width="1060" height="60" fill="var(--trim)"/>
      <polygon fill="var(--glass)" points="838,214 930,212 985,325 836,325"/>
    </g>
    <g class="wheels">
      <circle cx="332" cy="490" r="62" fill="var(--tyre)"/><circle cx="332" cy="490" r="34" fill="var(--hub)"/>
      <circle cx="1000" cy="490" r="62" fill="var(--tyre)"/><circle cx="1000" cy="490" r="34" fill="var(--hub)"/>
    </g>

    <g class="emblem">
      <circle cx="601" cy="281" r="160" fill="var(--ink-deep)" stroke="var(--gold)" stroke-width="4"/>
      <text class="txt brand-sub" x="601" y="240" text-anchor="middle">HARBOUR</text>
      <text class="txt brand-name" x="601" y="300" text-anchor="middle">ELECTRIC</text>
    </g>

    <g class="info-block">
      <text class="txt tagline" x="272" y="218" text-anchor="middle">YOUR LOCAL</text>
      <text class="txt tagline" x="272" y="246" text-anchor="middle">GAS &amp; ELECTRICAL</text>
      <rect x="93" y="252" width="335" height="30" fill="var(--gold)"/>
      <text class="txt service-band-text" x="260" y="273" text-anchor="middle">RESIDENTIAL &amp; COMMERCIAL SERVICES</text>
      <line x1="120" y1="294" x2="185" y2="294" stroke="var(--gold)" stroke-width="1.5"/>
      <line x1="362" y1="294" x2="428" y2="294" stroke="var(--gold)" stroke-width="1.5"/>
      <text class="txt web" x="274" y="299" text-anchor="middle">www.harbourelectric.ca</text>
      <circle cx="178" cy="340" r="15" fill="var(--gold)"/>
      <path d="M172,332 l4,-2 3,6 -3,2 q2,5 6,7 l2,-3 6,3 -2,4 q-10,1 -16,-17 z" fill="var(--ink)"/>
      <text class="txt phone" x="200" y="350">555-214-7730</text>
      <text class="txt licence" x="165" y="376">KRB# 4820917 / LMQ# 000562184</text>
    </g>

    <g class="partner-badge">
      <rect x="858" y="354" width="86" height="36" fill="var(--white)" stroke="var(--ink)" stroke-width="1"/>
      <text class="txt partner-name" x="901" y="370" text-anchor="middle">PELVORA</text>
      <text class="txt partner-sub" x="901" y="380" text-anchor="middle">SERVICE &amp; SALES</text>
      <text class="txt partner-sub" x="901" y="387" text-anchor="middle">EV Charger Installs</text>
    </g>
  </svg>

  <!-- Driver side (faces left) -->
  <svg class="van-side" viewBox="0 0 1187 600" xmlns="http://www.w3.org/2000/svg">
    <defs>
      <clipPath id="body-clip-b">
        <path transform="translate(1187,0) scale(-1,1)" d="M95,145 Q98,120 130,120 L905,120 Q960,124 990,200 L1035,330 Q1128,355 1140,400 L1146,470 Q1146,492 1120,492 L100,492 Q95,492 95,475 Z"/>
      </clipPath>
    </defs>
    <g class="van-body" clip-path="url(#body-clip-b)">
      <g transform="translate(1187,0) scale(-1,1)">
        <rect x="90" y="115" width="1060" height="385" fill="var(--white)"/>
        <polygon fill="var(--ink)" points="90,115 740,115 690,500 90,500"/>
        <polygon class="bolt" fill="var(--gold)" points="712,120 835,120 795,245 815,245 690,492 712,310 690,310"/>
        <rect x="90" y="440" width="1060" height="60" fill="var(--trim)"/>
        <polygon fill="var(--glass)" points="838,214 930,212 985,325 836,325"/>
      </g>
    </g>
    <g class="wheels">
      <circle cx="187" cy="490" r="62" fill="var(--tyre)"/><circle cx="187" cy="490" r="34" fill="var(--hub)"/>
      <circle cx="855" cy="490" r="62" fill="var(--tyre)"/><circle cx="855" cy="490" r="34" fill="var(--hub)"/>
    </g>

    <g class="emblem">
      <circle cx="588" cy="281" r="160" fill="var(--ink-deep)" stroke="var(--gold)" stroke-width="4"/>
      <text class="txt brand-sub" x="588" y="240" text-anchor="middle">HARBOUR</text>
      <text class="txt brand-name" x="588" y="300" text-anchor="middle">ELECTRIC</text>
    </g>

    <g class="info-block">
      <text class="txt tagline" x="915" y="218" text-anchor="middle">YOUR LOCAL</text>
      <text class="txt tagline" x="915" y="246" text-anchor="middle">GAS &amp; ELECTRICAL</text>
      <rect x="759" y="252" width="335" height="30" fill="var(--gold)"/>
      <text class="txt service-band-text" x="927" y="273" text-anchor="middle">RESIDENTIAL &amp; COMMERCIAL SERVICES</text>
      <line x1="760" y1="294" x2="825" y2="294" stroke="var(--gold)" stroke-width="1.5"/>
      <line x1="1002" y1="294" x2="1068" y2="294" stroke="var(--gold)" stroke-width="1.5"/>
      <text class="txt web" x="913" y="299" text-anchor="middle">www.harbourelectric.ca</text>
      <circle cx="822" cy="340" r="15" fill="var(--gold)"/>
      <path d="M816,332 l4,-2 3,6 -3,2 q2,5 6,7 l2,-3 6,3 -2,4 q-10,1 -16,-17 z" fill="var(--ink)"/>
      <text class="txt phone" x="844" y="350">555-214-7730</text>
      <text class="txt licence" x="808" y="376">KRB# 4820917 / LMQ# 000562184</text>
    </g>

    <g class="partner-badge">
      <rect x="243" y="354" width="86" height="36" fill="var(--white)" stroke="var(--ink)" stroke-width="1"/>
      <text class="txt partner-name" x="286" y="370" text-anchor="middle">PELVORA</text>
      <text class="txt partner-sub" x="286" y="380" text-anchor="middle">SERVICE &amp; SALES</text>
      <text class="txt partner-sub" x="286" y="387" text-anchor="middle">EV Charger Installs</text>
    </g>
  </svg>

</main>
</body>
</html>
```